Business card design for a debt inventory management software company

We need a business card design to help us move into the next phase of our business. We developed an innovative solution to help companies collect their bad debts. We are moving into a new era and branching out into new industries. We are open to design ideas but would like that they have a similar feel/look to our website and include our logo. https://www.lumoryx.com

Target Market(s)

Finance Industry, Telecom Industry, Utility Industry, Healthcare Industry, Insurance Industry

Industry/Entity Type

Software

Contact Information for Business Card

Include Name, Title, Phone, Email, website, address, and logo

Font styles to use
Sans Serif

Colors

Designer to choose colors to be used in the design.

Requirements
Must have
• A similar look and feel to our website. https://www.lumoryx.com

```html
<!DOCTYPE html>
<html lang="en">
<head>
<meta charset="utf-8">
<title>Lumoryx Software – Business Card</title>
<link rel="stylesheet" href="https://fonts.googleapis.com/css2?family=Raleway:wght@300;400;500&display=swap">
<style>
  :root {
    --backdrop: #262728;
    --card-navy: #3b4573;
    --card-navy-light: #48538a;
    --card-navy-dark: #313a63;
    --ink-light: #e9ecf6;
    --ink-soft: #cfd4e8;
    --line: #dfe3f1;
    --accent-red: #d3303a;
    --mark: #e9ecf6;
  }
  * { box-sizing: border-box; margin: 0; padding: 0; }
  html, body {
    width: 1200px; height: 900px; overflow: hidden;
    background: var(--backdrop);
    font-family: "Raleway", sans-serif;
  }
  .canvas { position: relative; width: 1200px; height: 900px; }

  .card {
    position: absolute; left: 280px; width: 640px; height: 366px;
    background: radial-gradient(ellipse at 40% 35%, var(--card-navy-light) 0%, var(--card-navy) 50%, var(--card-navy-dark) 100%);
    box-shadow: 0 18px 40px rgba(0,0,0,.55);
    overflow: hidden;
  }
  .card--front { top: 54px; }
  .card--back { top: 470px; }
  .card svg.rules { position: absolute; inset: 0; width: 100%; height: 100%; }

  .brand {
    position: absolute; display: flex; align-items: center; gap: 12px;
    color: var(--ink-light); font-weight: 300; white-space: nowrap; line-height: 1;
  }
  .brand__mark { width: 26px; height: 26px; background: var(--mark); border-radius: 2px; }
  .card--front .brand { left: 214px; top: 145px; font-size: 34px; }
  .card--back .brand { left: 64px; top: 284px; font-size: 24px; gap: 10px; }
  .card--back .brand__mark { width: 20px; height: 20px; }

  .front-web {
    position: absolute; left: 330px; top: 262px;
    color: var(--ink-soft); font-size: 12px; letter-spacing: 5px; font-weight: 400;
  }

  .person { position: absolute; right: 196px; top: 96px; text-align: right; color: var(--ink-light); }
  .person__name { font-size: 28px; font-weight: 400; letter-spacing: 1px; line-height: 1; }
  .person__title { font-size: 11px; font-weight: 500; letter-spacing: 1px; margin-top: 5px; }

  .contacts {
    position: absolute; right: 174px; top: 176px; text-align: right;
    color: var(--ink-light); font-size: 14px; font-weight: 400; list-style: none;
  }
  .contacts li { height: 27px; line-height: 27px; }
  .contacts li.address { line-height: 17px; padding-top: 5px; }
</style>
</head>
<body>
<main class="canvas">

  <section class="card card--front" aria-label="Card front">
    <svg class="rules" viewBox="0 0 640 366" aria-hidden="true">
      <line x1="0" y1="182" x2="198" y2="182" stroke="var(--line)" stroke-width="1"/>
      <circle cx="200" cy="182" r="3" fill="var(--line)"/>
      <circle cx="556" cy="160" r="3" fill="var(--line)"/>
      <line x1="558" y1="160" x2="640" y2="160" stroke="var(--line)" stroke-width="1"/>
    </svg>
    <div class="brand"><span class="brand__mark"></span><span class="brand__name">Lumoryx Software</span></div>
    <p class="front-web">www.yourwebsite.com</p>
  </section>

  <section class="card card--back" aria-label="Card back">
    <svg class="rules" viewBox="0 0 640 366" aria-hidden="true">
      <line x1="0" y1="296" x2="52" y2="296" stroke="var(--line)" stroke-width="1"/>
      <line x1="454" y1="90" x2="454" y2="148" stroke="var(--line)" stroke-width="1"/>
      <line x1="290" y1="162" x2="470" y2="162" stroke="var(--line)" stroke-width="1"/>
      <line x1="480" y1="150" x2="640" y2="150" stroke="var(--line)" stroke-width="1"/>
      <line x1="590" y1="150" x2="590" y2="300" stroke="var(--line)" stroke-width="1"/>
      <g stroke="var(--line)" stroke-width="1" fill="var(--line)">
        <line x1="478" y1="190" x2="548" y2="190"/><circle cx="478" cy="190" r="2.5"/>
        <line x1="478" y1="217" x2="548" y2="217"/><circle cx="478" cy="217" r="2.5"/>
        <line x1="478" y1="244" x2="548" y2="244"/><circle cx="478" cy="244" r="2.5"/>
        <line x1="478" y1="271" x2="548" y2="271"/><circle cx="478" cy="271" r="2.5"/>
      </g>
      <g fill="var(--card-navy)" stroke="var(--accent-red)" stroke-width="1.5">
        <circle cx="560" cy="190" r="11"/>
        <circle cx="560" cy="217" r="11"/>
        <circle cx="560" cy="244" r="11"/>
        <circle cx="560" cy="271" r="11"/>
      </g>
      <g fill="none" stroke="var(--ink-light)" stroke-width="1.1">
        <path d="M555 185 q0 8 8 10 l2 -2 -2.5 -2.5 -1.5 1.5 q-3 -1.5 -4 -4 l1.5 -1.5 -2.5 -2.5 z"/>
        <rect x="554" y="213" width="12" height="8"/><path d="M554 213 l6 5 6 -5"/>
        <circle cx="560" cy="244" r="6"/><path d="M554 244 h12 M560 238 q-4 6 0 12 M560 238 q4 6 0 12"/>
        <path d="M560 278 q-6 -6 -6 -10 a6 6 0 0 1 12 0 q0 4 -6 10 z"/><circle cx="560" cy="268" r="2"/>
      </g>
    </svg>
    <div class="brand"><span class="brand__mark"></span><span class="brand__name">Lumoryx Software</span></div>
    <div class="person">
      <p class="person__name">YOUR NAME</p>
      <p class="person__title">JOB TITLE</p>
    </div>
    <ul class="contacts">
      <li>000 000 0000</li>
      <li>youremail@xyz.com</li>
      <li>www.yourwebsite.com</li>
      <li class="address">Somewhere, Your City<br>ST 0000</li>
    </ul>
  </section>

</main>
</body>
</html>
```